New Book Cover Design Project

Book Cover with this title and sub title
Lessons Taught by the Old Orchard Hives
A pocket guide to careful spending and caring for nature.
Walter P. Kolb Ph. D.
Ruth P. Kolb
Picture below would be on the entire front cover. Words somehow incorporated for easy reading.

```html
<!DOCTYPE html>
<html lang="en">
<head>
<meta charset="utf-8">
<title>Lessons Taught by the Old Orchard Hives — Book Cover</title>
<link rel="stylesheet" href="https://fonts.googleapis.com/css2?family=Cinzel:wght@400;500&display=swap">
<style>
  :root {
    --forest-dark: #2c3725;
    --forest-mid: #3d4a2c;
    --meadow-green: #6d8a2a;
    --petal-yellow: #f4d20a;
    --petal-deep: #e0a800;
    --ink-light: #ffffff;
    --ink-soft: #f3f1e6;
  }
  * { margin: 0; padding: 0; box-sizing: border-box; }
  html, body {
    width: 840px;
    height: 1200px;
    overflow: hidden;
    background: var(--forest-dark);
  }
  .cover {
    position: relative;
    width: 840px;
    height: 1200px;
    overflow: hidden;
    font-family: 'Cinzel', serif;
    color: var(--ink-light);
  }
  .cover-photo {
    position: absolute;
    inset: 0;
    background:
      radial-gradient(ellipse 70% 28% at 52% 96%, var(--petal-yellow) 0%, var(--petal-deep) 45%, rgba(224,168,0,0) 75%),
      radial-gradient(ellipse 60% 20% at 50% 80%, rgba(244,210,10,0.95) 0%, rgba(244,210,10,0) 70%),
      radial-gradient(ellipse 40% 18% at 8% 72%, rgba(140,160,60,0.55) 0%, rgba(140,160,60,0) 70%),
      radial-gradient(ellipse 30% 14% at 95% 70%, rgba(110,130,40,0.45) 0%, rgba(110,130,40,0) 70%),
      linear-gradient(180deg, var(--forest-dark) 0%, var(--forest-dark) 42%, var(--forest-mid) 58%, var(--meadow-green) 78%, #8a9a1e 100%);
  }
  .title-block {
    position: absolute;
    top: 100px;
    left: 0;
    width: 100%;
    text-align: center;
  }
  .title-minor {
    display: block;
    font-size: 34px;
    font-weight: 400;
    letter-spacing: 0.5em;
    padding-left: 0.5em;
    line-height: 1;
  }
  .title-major {
    display: block;
    font-size: 74px;
    font-weight: 400;
    letter-spacing: 0.01em;
    line-height: 1;
  }
  .title-minor.first { margin-bottom: 14px; }
  .title-major.first { margin-bottom: 14px; }
  .title-minor.second { margin-bottom: 18px; }
  .subtitle {
    position: absolute;
    top: 400px;
    left: 40px;
    width: 760px;
    text-align: center;
    font-size: 24px;
    font-variant: small-caps;
    letter-spacing: 0.1em;
    line-height: 37px;
    color: var(--ink-soft);
  }
  .authors {
    position: absolute;
    top: 1088px;
    left: 0;
    width: 100%;
    text-align: center;
    font-size: 32px;
    line-height: 40px;
    color: var(--ink-light);
  }
</style>
</head>
<body>
  <main class="cover">
    <div class="cover-photo" role="img" aria-label="Close-up photograph of a pollen-covered honeybee on a bright yellow dandelion, dark green blurred background"></div>

    <h1 class="title-block">
      <span class="title-minor first">LESSONS</span>
      <span class="title-major first">TAUGHT BY THE</span>
      <span class="title-minor second">OLD</span>
      <span class="title-major">ORCHARD HIVES</span>
    </h1>

    <p class="subtitle">A pocket guide to careful spending<br>and caring for nature.</p>

    <p class="authors">
      Walter P. Kolb Ph. D.<br>
      Ruth P. Kolb
    </p>
  </main>
</body>
</html>
```